Birch Hollow Lodge & Harbour. A site that will sell our lifestyle and embody our vision.

We are after a fun interactive website for our property development.
Check out our ideas for layout and content.
Use stock videos and phots if we havent provide enough.
Ive attached our Logo.
We are easy to reach and work with. Love the crative process.1.Our Vision.. (This clicks through to vision page)
Nestled in the North East corner of Tesko Lake , Sk amidst thousands of acres of natural beauty, a unique community is taking shape. A community that connectS people, nature and play. A place to find those simpler times.

2.Explore..(This clicks through to explore page)
Discover a new life of adventure, on the lake fishing, in the bush on our trail system or maybe the local golf course.

3. Live Here..(This through to Live page)
Birch Hollow has everything you need to start living a full life based in a thriving community.
Slow down and get to know nature and your neighbors

Target Market(s)

35-65 Lake Life

Coding

Coded - Design and coding required

Number of Pages Required

5+ page

Font styles to use
Other font styles liked:
• Anntonio

Colors
00AB8E
00BBA5
67D7C9
C6EFE9
E9F9F6
F0912C
F2A743
F7CA91
FBE8D2
FDF5EE

Requirements
Nice to have
• Interactive

```html
<!DOCTYPE html>
<html lang="en">
<head>
<meta charset="utf-8">
<title>Birch Hollow Lodge &amp; Harbour</title>
<link rel="stylesheet" href="https://fonts.googleapis.com/css2?family=Antonio:wght@600;700&family=Rubik:wght@400;500&family=Montserrat:wght@400;500&display=swap">
<style>
  :root{
    --teal:#00AB8E;
    --teal-bright:#00BBA5;
    --teal-soft:#67D7C9;
    --teal-pale:#C6EFE9;
    --orange:#F0912C;
    --page:#F0F0F0;
    --forest:#034A3F;
    --ink:#454545;
    --body:#4a4a4a;
    --white:#ffffff;
  }
  *{box-sizing:border-box;margin:0;padding:0}
  html,body{width:1024px;height:1200px;overflow:hidden}
  body{position:relative;background:var(--page);font-family:"Rubik",sans-serif;color:var(--body)}
  .abs{position:absolute}

  /* hero */
  .hero{left:0;top:0;width:1024px;height:498px;
    background:linear-gradient(180deg,#4b5a3a 0%,#6b6a4a 25%,#2d5a6a 45%,#7d7866 62%,#a9a394 78%,#3b4a4f 100%)}
  .hero-shade{left:0;top:0;width:1024px;height:498px;background:rgba(40,30,20,.25)}
  .menu-btn{left:128px;top:21px;width:30px;height:27px;background:var(--teal);border-radius:2px}
  .menu-btn span{position:absolute;right:7px;height:2px;background:var(--white);border-radius:1px}
  .btn{display:flex;align-items:center;justify-content:center;color:var(--white);
    font-family:"Rubik",sans-serif;font-weight:500;font-size:8.5px;letter-spacing:.6px;text-transform:uppercase;border-radius:2px}
  .btn-book{left:727px;top:21px;width:77px;height:27px;background:var(--orange)}
  .btn-contact{left:810px;top:21px;width:87px;height:27px;background:var(--teal)}
  .brand-mark{left:412px;top:190px;width:200px;text-align:center}
  .brand-name{font-family:"Antonio",sans-serif;font-weight:700;color:var(--white);font-size:27px;letter-spacing:1px;line-height:1}
  .hero-brand{left:412px;top:232px;width:200px;text-align:center}
  .scroll-hint{left:504px;top:489px}

  /* features */
  .feature{top:567px;width:210px;text-align:center}
  .feature svg{display:block;margin:0 auto}
  .feature h2{font-family:"Antonio",sans-serif;font-weight:700;font-size:28px;color:var(--ink);margin-top:18px;line-height:1}
  .feature p{font-size:8.7px;line-height:12.7px;margin:10px auto 0;width:196px;color:var(--body)}
  .btn-main{left:474px;top:804px;width:77px;height:27px;background:var(--teal)}

  /* footer */
  .footer{left:0;top:930px;width:1024px;height:243px;background:var(--forest)}
  .foot-title{font-family:"Antonio",sans-serif;font-weight:700;font-size:18px;color:var(--white);letter-spacing:.3px;line-height:1}
  .foot-text{font-family:"Montserrat",sans-serif;font-size:10.2px;color:#e6efec;line-height:16.5px}
  .contact-row{display:flex;gap:8px;align-items:flex-start}
  .contact-row svg{flex:none;margin-top:2px}
  .links a{display:block;color:#e6efec;text-decoration:none}
  .links a.current{color:var(--orange);text-decoration:underline}
  .touch p{color:var(--teal-bright);font-family:"Montserrat",sans-serif;font-size:9.3px;line-height:13px;width:190px}
  .email{left:665px;top:1044px;width:231px;height:27px;background:var(--white);border-radius:2px;
    font-family:"Montserrat",sans-serif;font-size:9px;color:#8a8a8a;padding-left:16px;display:flex;align-items:center}
  .btn-sub{left:665px;top:1076px;width:105px;height:27px;background:var(--teal)}
  .bar{left:0;top:1173px;width:1024px;height:27px;background:var(--teal)}
  .copy{left:128px;top:1181px;font-family:"Montserrat",sans-serif;font-size:9.5px;color:var(--white)}
  .social{top:1177px;width:18px;height:18px;border-radius:50%;background:#0a9a80}
  .social.active{background:var(--orange)}
</style>
</head>
<body>

<div class="abs hero" role="img" aria-label="Photo of a resort pool with palm trees, slide and white parasols over loungers"></div>
<div class="abs hero-shade"></div>

<div class="abs menu-btn"><span style="top:8px;width:15px"></span><span style="top:13px;width:12px"></span><span style="top:18px;width:9px"></span></div>
<div class="abs btn btn-book">Book Now</div>
<div class="abs btn btn-contact">Contact Us</div>

<div class="abs hero-brand"><div class="brand-name">BIRCH HOLLOW</div></div>

<svg class="abs" style="left:0;top:455px" width="1024" height="45" viewBox="0 0 1024 45">
  <polygon points="342,43 512,8 683,43" fill="var(--teal)"/>
  <polygon points="330,45 512,15 694,45" fill="var(--page)"/>
</svg>
<svg class="abs scroll-hint" width="16" height="30" viewBox="0 0 16 30">
  <rect x="2" y="1" width="12" height="18" rx="6" fill="none" stroke="#555" stroke-width="1"/>
  <line x1="8" y1="5" x2="8" y2="9" stroke="#555" stroke-width="1"/>
  <line x1="8" y1="22" x2="8" y2="29" stroke="#555" stroke-width="1"/>
  <polyline points="5,26 8,29 11,26" fill="none" stroke="#555" stroke-width="1"/>
</svg>

<!-- features -->
<div class="abs feature" style="left:172px">
  <svg width="66" height="84" viewBox="0 0 66 84">
    <polygon points="1,12 33,1 65,12 65,83 1,83" fill="none" stroke="var(--teal-pale)" stroke-width="1.5"/>
    <g fill="var(--teal)" stroke="var(--teal)">
      <rect x="20" y="32" width="24" height="8" rx="2" transform="rotate(-20 32 36)"/>
      <line x1="32" y1="41" x2="24" y2="66" stroke-width="2"/>
      <line x1="32" y1="41" x2="40" y2="66" stroke-width="2"/>
      <line x1="32" y1="41" x2="32" y2="66" stroke-width="2"/>
    </g>
  </svg>
  <h2>OUR VISION</h2>
  <p>Nestled in the North East corner of Tesko Lake , Sk amidst thousands of acres of natural beauty, a unique community is taking shape. A community that connectS people, nature and play. A place to find those simpler times.</p>
</div>

<div class="abs feature" style="left:407px">
  <svg width="66" height="84" viewBox="0 0 66 84">
    <polygon points="1,12 33,1 65,12 65,83 1,83" fill="none" stroke="var(--teal-pale)" stroke-width="1.5"/>
    <circle cx="33" cy="45" r="16" fill="none" stroke="var(--teal)" stroke-width="2"/>
    <polygon points="33,31 36,42 47,45 36,48 33,59 30,48 19,45 30,42" fill="var(--teal)"/>
  </svg>
  <h2>EXPLORE</h2>
  <p>Discover&nbsp; a new life of adventure, on the lake fishing, in the bush on our trail system or maybe the local golf course.</p>
</div>

<div class="abs feature" style="left:641px">
  <svg width="66" height="84" viewBox="0 0 66 84">
    <polygon points="1,12 33,1 65,12 65,83 1,83" fill="none" stroke="var(--teal-pale)" stroke-width="1.5"/>
    <circle cx="33" cy="45" r="3.5" fill="var(--teal)"/>
    <g fill="none" stroke="var(--teal)" stroke-width="2.5" stroke-linecap="round">
      <path d="M26 38 a10 10 0 0 0 0 14"/><path d="M40 38 a10 10 0 0 1 0 14"/>
      <path d="M21 33 a17 17 0 0 0 0 24"/><path d="M45 33 a17 17 0 0 1 0 24"/>
    </g>
  </svg>
  <h2>LIVE HERE</h2>
  <p>Birch Hollow has everything you need to start living a full life based in a thriving community.</p>
</div>

<div class="abs btn btn-main">Book Now</div>

<!-- footer -->
<svg class="abs" style="left:0;top:893px" width="1024" height="38" viewBox="0 0 1024 38">
  <polygon points="342,37 512,1 683,37" fill="var(--teal)"/>
  <polygon points="355,38 512,9 670,38" fill="var(--forest)"/>
</svg>
<div class="abs footer"></div>

<div class="abs" style="left:128px;top:1050px"><div class="brand-name" style="font-size:20px">BIRCH HOLLOW</div></div>

<div class="abs" style="left:290px;top:981px">
  <div class="foot-title">CONATCT INFO</div>
  <div class="foot-text" style="margin-top:12px">
    <div class="contact-row"><svg width="10" height="12" viewBox="0 0 10 12"><path d="M5 0a5 5 0 0 1 5 5c0 3-5 7-5 7S0 8 0 5a5 5 0 0 1 5-5z" fill="var(--teal-bright)"/><circle cx="5" cy="5" r="2" fill="var(--forest)"/></svg><span>412 Alder Ridge Rd., Tesko Bay,<br>SK S0M 2T1</span></div>
    <div class="contact-row" style="margin-top:9px"><svg width="10" height="10" viewBox="0 0 10 10"><path d="M1 1l2-1 2 3-1.5 1.2a6 6 0 0 0 2.3 2.3L7 5l3 2-1 2C4 9 1 6 1 1z" fill="var(--teal-bright)"/></svg><span>(306) 555-0182</span></div>
    <div class="contact-row" style="margin-top:9px"><svg width="11" height="9" viewBox="0 0 11 9"><rect width="11" height="8" y="1" fill="var(--teal-bright)"/><polyline points="0,1 5.5,5 11,1" fill="none" stroke="var(--forest)"/></svg><span>hello@birchhollowlodge.com</span></div>
    <div class="contact-row" style="margin-top:9px"><svg width="11" height="11" viewBox="0 0 11 11"><circle cx="5.5" cy="5.5" r="5" fill="none" stroke="var(--teal-bright)" stroke-width="1.3"/><line x1="0.5" y1="5.5" x2="10.5" y2="5.5" stroke="var(--teal-bright)"/><ellipse cx="5.5" cy="5.5" rx="2" ry="5" fill="none" stroke="var(--teal-bright)"/></svg><span>live location</span></div>
  </div>
</div>

<div class="abs links" style="left:513px;top:981px">
  <div class="foot-title">QUICK LINK</div>
  <div class="foot-text" style="margin-top:12px">
    <a class="current" href="#">Home</a>
    <a href="#">Our Vision</a>
    <a href="#">Explore</a>
    <a href="#">Live Here</a>
    <a href="#">Contact Us</a>
    <a href="#">Privacy Policy</a>
    <a href="#">Terms &amp; Conditions</a>
  </div>
</div>

<div class="abs touch" style="left:665px;top:981px">
  <div class="foot-title">STAY IN TOUCH</div>
  <p style="margin-top:13px">Sign up to be the first to know about our deals and special offers.</p>
</div>
<div class="abs email">Your email address*</div>
<div class="abs btn btn-sub">Subscribe Now</div>

<div class="abs bar"></div>
<div class="abs copy">© 2023 Birch Hollow Lodge. All Right Reserved</div>
<div class="abs social" style="left:811px"></div>
<div class="abs social" style="left:834px"></div>
<div class="abs social active" style="left:856px"></div>
<div class="abs social" style="left:879px"></div>

</body>
</html>
```